Report Design

I am looking for a redesign of our monthly inspection reports we submit to our customers. I uploaded the current one we use (FernHollow) and also that of a competitor (Calm Ridge). I want to more copy the layout of the Calmridge report I attached but with more flow and design.

Requirements
Must have
• This has to be in a template format that we can modify the content every month.

```html
<!DOCTYPE html>
<html lang="en">
<head>
<meta charset="utf-8">
<title>Landscape, Irrigation &amp; Property Inspection Report</title>
<link href="https://fonts.googleapis.com/css2?family=Oswald:wght@400;500&family=Arimo:wght@400;700&display=swap" rel="stylesheet">
<style>
:root{
  --bg:#000;
  --paper:#fff;
  --green-dark:#176b36;
  --green:#1f9d48;
  --green-light:#5dbb46;
  --ink:#222;
  --frame:#22a64a;
}
*{box-sizing:border-box;margin:0;padding:0}
html,body{width:960px;height:1200px;overflow:hidden;background:var(--bg)}
body{position:relative;font-family:'Arimo',Arial,sans-serif;color:var(--ink)}
.report-page{position:absolute;width:389px;height:549px;background:var(--paper);overflow:hidden}
.p1{left:83px;top:42px}.p2{left:489px;top:42px}
.p3{left:83px;top:610px}.p4{left:489px;top:610px}

.brand{position:absolute;left:20px;top:60px;display:flex;align-items:center;gap:6px}
.brand-mark{width:11px;height:11px;background:var(--green)}
.brand-name{font-family:'Arimo',Arial,sans-serif;font-weight:700;font-size:19px;color:var(--ink);letter-spacing:-.4px}
.brand-sub{position:absolute;left:20px;top:92px;font-size:7.5px;font-weight:700}

.title-banner{position:absolute;left:143px;top:14px;width:246px;height:70px;background:var(--green-dark);
  clip-path:polygon(0 0,100% 0,100% 100%,22px 100%);color:#fff;font-family:'Oswald',sans-serif;
  font-size:20px;line-height:31px;padding:3px 0 0 42px;letter-spacing:.2px;white-space:nowrap}

.site-band{position:absolute;left:0;top:110px;width:389px;height:27px}
.site-name{position:absolute;left:0;top:0;width:270px;height:27px;background:var(--green);
  clip-path:polygon(0 0,calc(100% - 12px) 0,100% 100%,0 100%);color:#fff;font-weight:700;font-size:14px;line-height:27px;padding-left:13px;white-space:nowrap}
.site-month{position:absolute;left:268px;top:0;width:121px;height:27px;background:var(--green-light);
  clip-path:polygon(0 0,100% 0,100% 100%,12px 100%);color:#fff;font-weight:700;font-size:7.5px;line-height:27px;padding-left:20px}

.item-tab{position:absolute;left:0;height:20px;background:var(--green);color:#fff;font-weight:700;font-size:12px;line-height:20px;padding-left:14px;white-space:nowrap;
  clip-path:polygon(0 0,100% 0,calc(100% - 10px) 100%,0 100%)}
.item-tab .num{margin-right:10px}
.item-text{position:absolute;left:14px;width:172px;font-size:9.6px;line-height:12.5px}
.item-text.justify{text-align:justify}

.photo{position:absolute;border:3px solid var(--frame)}
.photo.lg{left:234px;width:137px;height:160px}
.photo.sm{left:17px;width:137px;height:84px}
.ph-grass{background:linear-gradient(180deg,#b9c6d2 0%,#c2a5a8 45%,#9a6f85 60%,#5b7a3a 100%)}
.ph-wall{background:linear-gradient(90deg,#d8d4c8 0%,#c9c4b6 55%,#6f7d55 80%,#a9aba6 100%)}
.ph-street{background:linear-gradient(180deg,#c3c9cf 0%,#6d6e6a 45%,#4f5a38 70%,#8a7164 100%)}
.ph-palms{background:linear-gradient(180deg,#e5e9ec 0%,#3f5a2a 45%,#7e8276 75%,#5a5b5d 100%)}
.ph-palmlot{background:linear-gradient(180deg,#bfc4c8 0%,#5a6a42 55%,#3c3f3a 100%)}
.ph-island{background:linear-gradient(180deg,#e7ebee 0%,#8aa06a 35%,#4d5a32 65%,#8d8c88 100%)}
.ph-tree{background:linear-gradient(180deg,#d9dee0 0%,#6d8a4a 35%,#4a5a33 60%,#9a9893 100%)}
.ph-coonties{background:linear-gradient(180deg,#4a5a2e 0%,#7a6a3a 50%,#a27a45 100%)}
.ph-mulch{background:linear-gradient(90deg,#d6d1c6 0%,#8b8a83 50%,#6e7053 100%)}
.ph-building{background:linear-gradient(90deg,#9fa8b0 0%,#dcd7cc 45%,#e4dfd5 70%,#bdbbb6 100%)}
.ph-copper{background:linear-gradient(180deg,#d9dde0 0%,#7e8a6a 45%,#8b2f3a 75%,#a7a59f 100%)}
.ph-walk{background:linear-gradient(180deg,#ccd1d5 0%,#6f8a4c 40%,#b7b4aa 60%,#a02a3a 85%)}

.footer{position:absolute;left:0;top:510px;width:389px;height:39px}
.footer-left{position:absolute;left:0;top:0;width:255px;height:39px;background:var(--green);
  clip-path:polygon(0 0,calc(100% - 24px) 0,100% 100%,0 100%);color:#fff;font-size:7.4px;line-height:9.5px;padding:3px 0 0 17px;white-space:nowrap}
.footer-left strong{display:block}
.footer-right{position:absolute;left:251px;top:0;width:138px;height:39px;background:var(--green);
  clip-path:polygon(0 0,100% 0,100% 100%,24px 100%);color:#fff;font-size:7.4px;line-height:9.5px;padding:3px 20px 0 0;text-align:right}
.footer-right .page-no{display:block;margin-top:4px}
</style>
</head>
<body>

<!-- Page 1 -->
<section class="report-page p1">
  <div class="brand"><span class="brand-mark"></span><span class="brand-name">FernHollow</span></div>
  <div class="brand-sub">Landscape and Maintenance, Inc.</div>
  <div class="title-banner">LANDSCAPE, IRR.&amp;<br>PROPERTY INSPECTION</div>
  <div class="site-band"><div class="site-name">Gardens on Westbrook POA &amp; Retail</div><div class="site-month">Month of November</div></div>

  <div class="item-tab" style="top:151px;width:181px"><span class="num">1.</span>Grasses Throughout:</div>
  <p class="item-text justify" style="top:177px">Right now the Muhly grass is blooming and looks great. The crew went around and trimmed them all up so they look fresh and clean. There were some of the types that were not blooming, that we trimmed back farther.</p>
  <div class="photo sm ph-wall" style="top:271px" role="img" aria-label="Ornamental grasses trimmed along a building wall"></div>
  <div class="photo lg ph-grass" style="top:148px" role="img" aria-label="Pink blooming Muhly grass bed with a tree behind"></div>

  <div class="item-tab" style="top:370px;width:120px"><span class="num">2.</span>Flowers:</div>
  <p class="item-text" style="top:400px">Both main entrances are in need of fresh flowers.</p>
  <div class="photo lg ph-street" style="top:343px" role="img" aria-label="Main entrance median bed by a crosswalk"></div>

  <footer class="footer">
    <div class="footer-left"><strong>Landscape and Grounds Maintenance</strong>Division, 1420 Orchard Lane, Maple Glen, FL 30000</div>
    <div class="footer-right">Ph: 555-013-7781<br>Fax 555-018-2245<span class="page-no">PAGE-01</span></div>
  </footer>
</section>

<!-- Page 2 -->
<section class="report-page p2">
  <div class="brand"><span class="brand-mark"></span><span class="brand-name">FernHollow</span></div>
  <div class="brand-sub">Landscape and Maintenance, Inc.</div>
  <div class="title-banner">LANDSCAPE, IRR.&amp;<br>PROPERTY INSPECTION</div>
  <div class="site-band"><div class="site-name">Gardens on Westbrook POA &amp; Retail</div><div class="site-month">Month of November</div></div>

  <div class="item-tab" style="top:151px;width:191px"><span class="num">3.</span>Palms Need Trimming:</div>
  <p class="item-text justify" style="top:177px">All the Palms could use a trimming, there are dead frons and some hanging seed pods and boots. Let us know if and when you would like to get this scheduled.</p>
  <div class="photo sm ph-palmlot" style="top:271px" role="img" aria-label="Palm trees beside a parking lot"></div>
  <div class="photo lg ph-palms" style="top:148px" role="img" aria-label="Row of palms along a median road"></div>

  <div class="item-tab" style="top:370px;width:104px"><span class="num">4.</span>Fill In:</div>
  <p class="item-text" style="top:400px">We should fill this corner in where truck run over the corner with additional plants.</p>
  <div class="photo lg ph-island" style="top:343px" role="img" aria-label="Curbed planting island with a damaged corner"></div>

  <footer class="footer">
    <div class="footer-left"><strong>Landscape and Grounds Maintenance</strong>Division, 1420 Orchard Lane, Maple Glen, FL 30000</div>
    <div class="footer-right">Ph: 555-013-7781<br>Fax 555-018-2245<span class="page-no">PAGE-02</span></div>
  </footer>
</section>

<!-- Page 3 -->
<section class="report-page p3">
  <div class="brand"><span class="brand-mark"></span><span class="brand-name">FernHollow</span></div>
  <div class="brand-sub">Landscape and Maintenance, Inc.</div>
  <div class="title-banner">LANDSCAPE, IRR.&amp;<br>PROPERTY INSPECTION</div>
  <div class="site-band"><div class="site-name">Gardens on Westbrook POA…cont</div><div class="site-month">Month of November</div></div>

  <div class="item-tab" style="top:153px;width:160px"><span class="num">5.</span>Fill in Coonties:</div>
  <p class="item-text" style="top:179px">Coonties need to be filled in here. As well as side of Burger Barn.</p>
  <div class="photo sm ph-coonties" style="top:270px" role="img" aria-label="Browning coontie plants needing replacement"></div>
  <div class="photo lg ph-tree" style="top:149px" role="img" aria-label="Parking lot island with a tree and shrubs"></div>

  <div class="item-tab" style="top:370px;width:110px"><span class="num">6.</span>Mulch:</div>
  <p class="item-text" style="top:400px">Overall the place could use fresh mulch, or we could just mulch these washed out areas that are an eye sore.</p>
  <div class="photo lg ph-mulch" style="top:343px" role="img" aria-label="Washed out mulch bed along a building"></div>

  <footer class="footer">
    <div class="footer-left"><strong>Landscape and Grounds Maintenance</strong>Division, 1420 Orchard Lane, Maple Glen, FL 30000</div>
    <div class="footer-right">Ph: 555-013-7781<br>Fax 555-018-2245<span class="page-no">PAGE-03</span></div>
  </footer>
</section>

<!-- Page 4 -->
<section class="report-page p4">
  <div class="brand"><span class="brand-mark"></span><span class="brand-name">FernHollow</span></div>
  <div class="brand-sub">Landscape and Maintenance, Inc.</div>
  <div class="title-banner">LANDSCAPE, IRR.&amp;<br>PROPERTY INSPECTION</div>
  <div class="site-band"><div class="site-name">Gardens on Westbrook POA…cont</div><div class="site-month">Month of November</div></div>

  <div class="item-tab" style="top:147px;width:110px"><span class="num">7.</span>Pruning:</div>
  <p class="item-text" style="top:173px">All the little palms have been pruned up to look clean</p>
  <div class="photo lg ph-building" style="top:143px" role="img" aria-label="Small pruned palms along a building walkway"></div>

  <div class="item-tab" style="top:347px;width:146px"><span class="num">8.</span>Plants fillingin:</div>
  <p class="item-text" style="top:376px">The copper plants and Jasmine are all filling in nicely</p>
  <div class="photo sm ph-walk" style="top:418px" role="img" aria-label="Red copper plants beside a sidewalk"></div>
  <div class="photo lg ph-copper" style="top:343px" role="img" aria-label="Copper plants and jasmine under a palm"></div>

  <footer class="footer">
    <div class="footer-left"><strong>Landscape and Grounds Maintenance</strong>Division, 1420 Orchard Lane, Maple Glen, FL 30000</div>
    <div class="footer-right">Ph: 555-013-7781<br>Fax 555-018-2245<span class="page-no">PAGE-04</span></div>
  </footer>
</section>

</body>
</html>
```